New Business Card Design Project

I would like my card design to look exactly like the logo, design, layout, and print of the current attached file. The only change I would like made would be for the print to say THE KMW GROUP instead of THE HALLORAN GROUP. Basically, just replace his group name with my group name. I would also like the backgroud to be the same texture and color as the attached file. I love the dark blue lettering and house logo on the card.

I am completely open to the rest of the card design. I just want something clean and simple. Only basic contact info required on the card. Maybe just name: Kyle M Warrick and cell # 555.914.2087 and email kyle@orchidhomesagent.com

```html
<!DOCTYPE html>
<html lang="en">
<head>
<meta charset="utf-8">
<title>The KMW Group — Business Card</title>
<link rel="stylesheet" href="https://fonts.googleapis.com/css2?family=Montserrat:wght@300;400&family=Inter:wght@400;700&display=swap">
<style>
  :root {
    --backdrop: #2b2b2e;
    --paper: #f4f4f2;
    --paper-shade: #ebebe8;
    --ink: #1b1f47;
  }
  * { box-sizing: border-box; margin: 0; padding: 0; }
  html, body { width: 1200px; height: 800px; overflow: hidden; }
  body {
    background: var(--backdrop);
    position: relative;
    font-family: "Montserrat", sans-serif;
    color: var(--ink);
  }
  .card {
    position: absolute;
    top: 252px;
    width: 520px;
    height: 297px;
    background: radial-gradient(circle at 30% 25%, var(--paper) 0%, var(--paper) 55%, var(--paper-shade) 100%);
    box-shadow: 0 18px 40px rgba(0,0,0,0.45);
  }
  .card--front { left: 50px; }
  .card--back { left: 630px; }

  /* Front side */
  .lockup {
    position: absolute;
    left: 150px;
    top: 118px;
    display: flex;
    align-items: center;
    gap: 16px;
  }
  .lockup__mark {
    width: 46px;
    height: 46px;
    background: var(--ink);
  }
  .group-name {
    font-family: "Montserrat", sans-serif;
    font-weight: 300;
    letter-spacing: 0.16em;
    line-height: 1.1;
    text-transform: uppercase;
    color: var(--ink);
  }
  .lockup .group-name { font-size: 24px; }

  /* Back side */
  .back__mark {
    position: absolute;
    right: 44px;
    top: 34px;
    width: 150px;
    height: 150px;
    background: var(--ink);
  }
  .back__info {
    position: absolute;
    left: 40px;
    top: 98px;
  }
  .back__info .group-name { font-size: 25px; }
  .person {
    margin-top: 22px;
    font-family: "Inter", sans-serif;
    font-weight: 700;
    font-size: 15px;
  }
  .contact {
    list-style: none;
    margin-top: 14px;
    font-family: "Inter", sans-serif;
    font-size: 12px;
    line-height: 1.7;
  }
  .contact li { display: flex; align-items: center; gap: 7px; }
  .contact svg { width: 11px; height: 11px; flex: none; }
</style>
</head>
<body>
  <section class="card card--front" aria-label="Business card front">
    <div class="lockup">
      <span class="lockup__mark" aria-hidden="true"></span>
      <p class="group-name">The<br>KMW Group</p>
    </div>
  </section>

  <section class="card card--back" aria-label="Business card back">
    <span class="back__mark" aria-hidden="true"></span>
    <div class="back__info">
      <p class="group-name">The<br>KMW Group</p>
      <p class="person">Kyle M Warrick</p>
      <ul class="contact">
        <li>
          <svg viewBox="0 0 12 12" aria-hidden="true"><rect x="3" y="0.8" width="6" height="10.4" rx="1" fill="none" stroke="currentColor" stroke-width="1.2"/><line x1="5" y1="9.3" x2="7" y2="9.3" stroke="currentColor" stroke-width="1"/></svg>
          <span>555.914.2087</span>
        </li>
        <li>
          <svg viewBox="0 0 12 12" aria-hidden="true"><rect x="0.5" y="2" width="11" height="8" fill="currentColor"/><polyline points="0.8,2.4 6,6.6 11.2,2.4" fill="none" stroke="#f4f4f2" stroke-width="1"/></svg>
          <span>kyle@orchidhomesagent.com</span>
        </li>
      </ul>
    </div>
  </section>
</body>
</html>
```